Flyer-Design für Betreuer von Altenwohn- und Pflegeheimen
Zielgruppe
Die vaxo-pro GmbH betreut Altenwohn- und Pflegeheime im Bereich Arbeitsschutz.
Die Bereiche sind:
- Beratung & Schulung für Arbeitssicherheit, Erste Hilfe und Brandschutz
- Prüfung von Arbeitsmitteln und Medizingeräten
- Reparatur& Wartung von Elektrogeräten
- ein Partner für die 'Lösung aus einer Hand'
Die Zielgruppe sind die Betreiber (Inhaber) und Leitungen von Pflegeeinrichtungen für ältere Menschen und MEnschen mit Behidnerungen
Aufgabenstellung
Das Format soll quadratisch analog dem Logo der vaxo-pro GmbH mit einer Seitenlänge von 210mm sein (Breite DIN A4). Der Folder soll einmal gefaltet sein..
Das Logo beschreibt die Leistungen der vaxo-pro
- linkes oberes Quadrat = 'Beratung&Schulung'
- rechtes oberes Quadrat = 'Prüfung'
- linkes unteres Quadrat = 'Reparatur & Wartung'
- rechtes unteres Quadrat mit dem Haken = 'ein Partner ('...alles aus einer Hand!' <-- wobei mir persönlich diese Wortwahl nicht gefällt')
Der Folder soll auf der ersten Seite beim Leser das Gefühl wecken: 'Das MUSS ich lesen...' <-- Neugierde wecken.
Die beiden Innenseiten sollen die jeweiligen Quadrate der Leistungen beschreiben (siehe oben)
Die Rückseite enthält Angaben zu Referenzen und die Kontaktdaten.
Die Referenzen sollen 'allgemein' gehalten werden:
• kommunale Betreiber
• gemeinnützige Betreiber mit vielen Einrichtungen in ganz Bayern
• viele kleine Einrichtungen mit wenigen Betten ebenso wie
• private große Betreiber mit 1500 Pflegeplätzen und mehr
Karte mit Bullets von Bayern (siehe hochgeladene Datei) - vorerst dieses Bild, in der finalen Version soll diese Karte nicht so sehr nach Plurimo aussehen.
Weieter habe jetzt noch Texte als Word-Datei hinzugefügt...

```html
<!DOCTYPE html>
<html lang="de">
<head>
<meta charset="utf-8">
<title>vaxo-pro Folder</title>
<link href="https://fonts.googleapis.com/css2?family=Ubuntu:wght@300;400&family=Carlito:wght@400&display=swap" rel="stylesheet">
<style>
:root{
  --yellow:#f9b91c;
  --ink:#5f5f5f;
  --ink-soft:#6e6e6e;
  --rule:#8a8a8a;
  --paper:#ffffff;
  --head:"Ubuntu",sans-serif;
  --body:"Carlito","Ubuntu",sans-serif;
}
*{box-sizing:border-box;margin:0;padding:0}
html,body{width:753px;height:1200px;overflow:hidden;background:#fff}
.canvas{position:relative;width:753px;height:1200px}
.page{position:absolute;background:var(--paper);box-shadow:0 1px 5px rgba(0,0,0,.35)}
.page>*{position:absolute}
.arrows{left:0;top:0;width:100%;height:100%;pointer-events:none}
.brand{font-family:var(--head);font-weight:300;color:var(--ink);font-size:15px;display:flex;align-items:center;gap:4px;line-height:1}
.brand-mark{width:11px;height:11px;background:var(--yellow);display:inline-block}
.txt{font-family:var(--body);color:var(--ink);font-size:6.3px;line-height:8.4px}
.accent{color:var(--yellow)}
.headline{font-family:var(--head);font-weight:300;color:var(--ink);font-size:17px;line-height:19px;letter-spacing:.3px}
.photo{display:block}
.caption{font-family:var(--body);color:var(--ink);font-size:4.8px}
.section-title{font-family:var(--head);font-weight:300;color:var(--ink);font-size:10px}
.bullets{font-family:var(--body);color:var(--ink-soft);font-size:5px;line-height:7px;list-style:none}
.bullets li{padding-left:4.5px;text-indent:-4.5px}
.bullets li::before{content:"• "}
.bullets.spaced li{margin-bottom:7px}
.tagline{font-family:var(--head);font-weight:300;color:var(--yellow);font-size:12.5px;line-height:16px;text-align:center}
.contact{font-family:var(--body);color:var(--ink);font-size:7.5px;line-height:9.8px}
.partner-box{background:var(--yellow);color:#fff;padding:3px 5px}
.partner-box h3{font-family:var(--head);font-weight:300;font-size:9.5px;line-height:10px}
.partner-box h3 span{display:block;text-align:right;padding-right:5px}
.partner-box ul{font-family:var(--body);font-size:4.8px;line-height:7.3px;list-style:none;margin-top:3px}
.partner-box li{padding-left:4px;text-indent:-4px}
.partner-box li::before{content:"• "}
.emblem{background:var(--yellow)}
.grid{display:grid;grid-template-columns:repeat(3,1fr);grid-template-rows:repeat(3,1fr);width:100%;height:100%;border:1px solid var(--rule)}
.cell{border:0.5px solid var(--rule);font-family:var(--body);color:var(--ink);font-size:7.5px;line-height:9.4px;padding:0 4px;display:flex;align-items:flex-start}
.cell.highlight{border-color:var(--yellow)}
</style>
</head>
<body>
<div class="canvas">

  <!-- Aussenseite: Rückseite + Titel -->
  <section class="page page-outer" style="left:196px;top:29px;width:349px;height:348px">
    <div class="brand" style="left:15px;top:15px"><span class="brand-mark"></span>vaxo-pro</div>
    <p class="txt" style="left:31px;top:39px">vaxo-pro GmbH<br>Lindenweg 12<br>85000 Musterau</p>
    <p class="txt" style="left:31px;top:72px">Telefon: <span class="accent">+49 (8000) 41527-0</span><br>E-Mail:&nbsp;&nbsp; <span class="accent">info@vaxo-pro.de</span></p>
    <div class="txt" style="left:31px;top:120px;width:130px">
      <span class="accent">Referenzen</span><br>
      • kommunale Betreiber<br>
      • gemeinnützige Betreiber mit vielen Einrichtungen in ganz Bayern<br>
      • viele kleine Einrichtungen mit wenigen Betten ebenso wie private große Betreiber mit 1500 Pflegeplätzen und mehr
    </div>
    <div class="photo" role="img" aria-label="Karte von Bayern mit orangefarbenen Standortmarkierungen der betreuten Einrichtungen" style="left:25.5px;top:210px;width:136px;height:83px;background:linear-gradient(135deg,#e4e9d8,#d9e0cb 60%,#e8ead9)"></div>
    <p class="caption" style="left:25.5px;top:296px">Kartendaten © 2018 GeoKarta (©2009) Plurimo</p>

    <div class="brand" style="left:187px;top:15px"><span class="brand-mark"></span>vaxo-pro</div>
    <h1 class="headline" style="left:186px;top:35px">Professionell,<br>Effizient und Sicher!</h1>
    <p class="txt" style="left:186px;top:84px;width:120px">Mit vaxo-pro haben Sie einen starken, zuverlässigen Partner, der sich allen Bereichen annimmt.</p>
    <div class="photo" role="img" aria-label="Foto: jubelnde Frau mit erhobenen Armen an einem Schreibtisch mit Laptop und roter Tasse" style="left:184px;top:116.5px;width:116px;height:150px;background:linear-gradient(160deg,#8d9a98,#77807f 55%,#c9c9c6)"></div>
    <p class="headline" style="left:184px;top:277px">Überzeugen<br>Sie sich selbst!</p>
    <svg class="arrows" viewBox="0 0 349 348" aria-hidden="true">
      <path d="M297 308 Q318 306 336 297" fill="none" stroke="var(--yellow)" stroke-width="1"/>
      <path d="M328 296 L336 297 L332 303" fill="none" stroke="var(--yellow)" stroke-width="1"/>
    </svg>
  </section>

  <!-- Innenseiten: Leistungen -->
  <section class="page page-inner" style="left:196px;top:407px;width:349px;height:344px">
    <h2 class="section-title" style="left:13px;top:11px">Beratung &amp; Schulung</h2>
    <ul class="bullets spaced" style="left:13px;top:31px;width:95px">
      <li>Betreuung als externe Fachkraft für Arbeitssicherheit und Brandschutz</li>
      <li>Schulung der Mitarbeiter im Umgang mit aktiven Medizinprodukten bzw. Hilfsmitteln</li>
      <li>Unterstützung bei Themen zum Qualitätsmanagement und zur Prozessgestaltung</li>
    </ul>
    <p class="tagline" style="left:120px;top:33px;width:112px">Unsere Leistungen<br>auf einen Blick!</p>
    <h2 class="section-title" style="left:232px;top:11px">Prüfung - Inspektion</h2>
    <ul class="bullets" style="left:232px;top:31px;width:108px;line-height:8.2px">
      <li>sicherheitstechnische Überprüfung der aktiven Medizinprodukte / Hilfsmittel</li>
      <li>Prüfung der elektrischen Betriebsmittel (Haus- und Küchengeräte, Werkzeuge, bewohnereigene Geräte)</li>
      <li>Prüfung der gesamten elektrischen Anlage inklusive Thermografie (Wärmbildkamera)</li>
      <li>Erstellung eines Bestandsverzeichnisses</li>
      <li>Mängelliste und Angebot zur Behebung</li>
    </ul>
    <div class="photo" role="img" aria-label="Foto: Person im Anzug arbeitet im Freien an einem Laptop auf einem Holztisch" style="left:13.5px;top:128px;width:92px;height:92px;background:linear-gradient(150deg,#7c8a6a,#4b5249 55%,#2f3236)"></div>
    <div class="emblem" style="left:169px;top:177px;width:42px;height:41px"></div>
    <p class="contact" style="left:235.5px;top:141px">Informieren sie sich auf<br>unserer Homepage:<br><span class="accent">www.vaxo-pro.de</span></p>
    <p class="contact" style="left:235.5px;top:181px">Oder rufen Sie uns gerne an!<br><span class="accent">Telefon: +49 (8000) 41527-0</span></p>
    <h2 class="section-title" style="left:13px;top:234px">Wartung - Reparatur</h2>
    <ul class="bullets" style="left:13px;top:254px;width:100px;line-height:8.2px">
      <li>herstellerunabhängiger Service für Medizinprodukte / Hilfsmittel, wie z. B.</li>
      <li>Pflegebetten</li>
      <li>Steckbeckenspülen mit Nachweis der Desinfektionsleitung</li>
      <li>Decken-/Tuch-/Sitzlifter / Aufstehhilfen</li>
      <li>Pflegebadewannen</li>
      <li>Sauerstoffkonzentratoren</li>
      <li>diverse weitere Geräte</li>
    </ul>
    <div class="partner-box" style="left:230px;top:231px;width:112px;height:107px">
      <h3>Viele Themen<span>Ein Partner</span></h3>
      <ul>
        <li>Koordination aller Termine und Fälligkeiten</li>
        <li>reibungslose Prüfabläufe ohne wesentlicher Störung des Tagesgeschäftes</li>
        <li>wirtschaftliche Mängelbeseitigung</li>
        <li>Inventarisierung durch eigenes Kennzeichnungs- und Dokumentationssystem</li>
        <li>vaxo-ONLINE – aktuelle Informationen und Dokumentationen Online auf einen Klick</li>
      </ul>
    </div>
    <svg class="arrows" viewBox="0 0 349 344" aria-hidden="true">
      <path d="M123 86 Q170 92 217 85" fill="none" stroke="var(--yellow)" stroke-width="1"/>
      <path d="M210 79 L218 85 L212 93" fill="none" stroke="var(--yellow)" stroke-width="1"/>
      <path d="M213 103 Q120 95 95 170 Q88 200 83 221" fill="none" stroke="var(--yellow)" stroke-width="1"/>
      <path d="M78 214 L83 222 L89 215" fill="none" stroke="var(--yellow)" stroke-width="1"/>
      <path d="M114 238 Q170 260 227 243" fill="none" stroke="var(--yellow)" stroke-width="1"/>
      <path d="M219 237 L227 243 L220 250" fill="none" stroke="var(--yellow)" stroke-width="1"/>
      <path d="M262 249 Q270 254 277 251" fill="none" stroke="#fff" stroke-width=".7"/>
      <path d="M274 248 L277 251 L274 254" fill="none" stroke="#fff" stroke-width=".7"/>
    </svg>
  </section>

  <!-- Nutzen-Seite -->
  <section class="page page-benefits" style="left:193px;top:783px;width:351px;height:351px">
    <div class="grid" style="left:0;top:0">
      <div class="cell" style="padding:41px 4px 0 13px">• mehr Sicherheit<br>für Mitarbeiter und Bewohner durch geschultem Umgang der Mitarbeiter mit Ihren Medizinprodukten</div>
      <div class="cell" style="justify-content:center;padding-top:33px"><p class="tagline" style="font-size:12.5px">Was Sie mit uns<br>erreichen!</p></div>
      <div class="cell" style="padding-top:44px">• Minimieren der Unfallgefahr und Gewährleistung der Sicherheit Ihrer Mitarbeiter und Bewohner</div>
      <div class="cell" style="padding:31px 4px 0 10px">• detaillierter Überblick zum Ist-Zustand Ihrer technischen Geräte und Anlagen</div>
      <div class="cell" style="position:relative"><span class="emblem" style="position:absolute;left:54px;top:61px;width:42px;height:41px"></span></div>
      <div class="cell" style="padding:31px 4px 0 11px">• Erfüllung von gesetzlichen, berufsgenossenschaftlichen und versicherungstechnischen Vorgaben erhöhen Ihre Betreibersicherheit</div>
      <div class="cell" style="padding:33px 4px 0 7px">• geregelte Zuständigkeiten und straff organisierte, effiziente Prozessabläufe erhöhen Ihre Wirtschaftlichkeit</div>
      <div class="cell" style="padding-top:33px">• kompetente Unterstützung zu vielen Themen und Fragen rund um Ihre Pflegeeinrichtung</div>
      <div class="cell highlight" style="padding-top:33px">• geregelte Zuständigkeiten und straff organisierte, effiziente Prozessabläufe erhöhen Ihre Wirtschaftlichkeit</div>
    </div>
  </section>

</div>
</body>
</html>
```